Graphic Design for a Info Card

We would like a graphic design for an info card . We would like the colours to correspond to our logo , you can add in the colours navy blue or yellow if you would like. We would like it to have the following information. We want something that really pops. We would like the size to be 4 1/2 x 6 .

ATTENTION!! Delivery Promo! Order from us on the @hopmorsel app or @vantrelcourier app on FRIDAYS and receive a FREE Sample of our one of our meal prep meals in your bag!
DID YOU KNOW?! Meal Prep is another great service that we offer. Saving you time, promoting your health, and best of all providing a delicious lunch . You can find more info on our website www.marlowpantry.example . All orders are available for delivery or pickup!

```html
<!DOCTYPE html>
<html lang="en">
<head>
<meta charset="utf-8">
<title>Marlow Info Card – Front and Back</title>
<link rel="stylesheet" href="https://fonts.googleapis.com/css2?family=Lexend:wght@300;400;500;700&display=swap">
<style>
  :root {
    --navy: #143d59;
    --green: #93c01f;
    --grey: #9b9b9b;
    --white: #ffffff;
    --label: #2d2d2d;
  }
  * { margin: 0; padding: 0; box-sizing: border-box; }
  html, body { width: 1200px; height: 1200px; overflow: hidden; background: var(--white); }
  body { position: relative; font-family: "Lexend", sans-serif; }

  .card { position: absolute; top: 220px; width: 546px; height: 728px; background: var(--grey); overflow: hidden; }
  .card--front { left: 35px; }
  .card--back { left: 626px; }
  .band { position: absolute; background: var(--green); }
  .panel { position: absolute; left: 42px; top: 45px; width: 462px; height: 639px; background: var(--navy); }

  /* front */
  .band--front-left { left: 0; top: 88px; width: 42px; height: 640px; }
  .band--front-bottom { left: 0; top: 684px; width: 459px; height: 44px; }
  .front-brand { position: absolute; left: 0; right: 0; top: 292px; text-align: center; }
  .front-brand__name { font-size: 66px; font-weight: 500; color: var(--grey); letter-spacing: 4px; line-height: 1; }
  .front-brand__tagline { margin-top: 12px; font-size: 20px; font-weight: 700; color: var(--green); letter-spacing: 0.5px; }

  /* back */
  .band--back-top { left: 87px; top: 0; width: 459px; height: 45px; }
  .band--back-right { left: 504px; top: 0; width: 42px; height: 641px; }
  .promo-strip { position: absolute; left: 42px; top: 605px; width: 504px; height: 36px; background: var(--green);
    color: var(--navy); font-weight: 700; font-size: 17.5px; line-height: 36px; padding-left: 25px; letter-spacing: -0.2px; }

  .back-brand { position: absolute; right: 24px; top: 20px; text-align: right; }
  .back-brand__name { font-size: 28px; font-weight: 500; color: var(--grey); letter-spacing: 2px; line-height: 1; }
  .back-brand__tagline { margin-top: 4px; font-size: 8.5px; font-weight: 700; color: var(--green); }

  .heading { position: absolute; left: 27px; font-size: 25px; font-weight: 400; color: var(--green); line-height: 1; }
  .heading--attention { top: 142px; }
  .heading--know { top: 330px; }

  .delivery { position: absolute; left: 27px; top: 178px; width: 190px; color: var(--white); font-size: 17.5px; font-weight: 400; line-height: 23px; }
  .delivery strong { font-weight: 700; }

  .friday-box { position: absolute; left: 213px; top: 164px; width: 230px; height: 104px; border: 1px solid var(--grey); border-top: none; }
  .friday-box__rule { position: absolute; top: 0; height: 1px; background: var(--grey); }
  .friday-box__rule--left { left: 0; width: 12px; }
  .friday-box__rule--right { right: 0; width: 10px; }
  .friday-box__small { position: absolute; color: var(--white); font-size: 11.5px; font-weight: 300; white-space: nowrap; }
  .friday-box__lead { left: 10px; top: 7px; }
  .friday-box__days { position: absolute; left: 53px; top: -18px; font-size: 40px; color: var(--green); line-height: 1; }
  .friday-box__receive { left: 10px; top: 27px; }
  .friday-box__free { position: absolute; left: 91px; top: 18px; font-size: 20px; color: var(--green); line-height: 1; white-space: nowrap; }
  .friday-box__detail { left: 10px; top: 42px; }
  .friday-box__bag { position: absolute; left: 8px; top: 52px; font-size: 46px; color: var(--green); line-height: 1; white-space: nowrap; }

  .know-body { position: absolute; left: 27px; top: 364px; width: 420px; color: var(--white); font-size: 16.5px; font-weight: 300; line-height: 23px; letter-spacing: -0.2px; }

  .more-info { position: absolute; left: 27px; top: 495px; width: 408px; height: 60px; }
  .more-info__label { position: absolute; left: 0; top: 0; color: var(--grey); font-size: 18px; font-weight: 300; white-space: nowrap; }
  .more-info__rule { position: absolute; height: 1px; background: var(--grey); }
  .more-info__rule--top { left: 244px; right: 0; top: 13px; }
  .more-info__rule--bottom { left: 0; width: 142px; top: 40px; }
  .more-info__site { position: absolute; right: 0; top: 28px; color: var(--white); font-size: 18px; font-weight: 300; letter-spacing: 1.5px; white-space: nowrap; }
  .more-info__site span { color: var(--green); }

  .side-label { position: absolute; top: 962px; font-size: 23px; font-weight: 700; color: var(--label); }
  .side-label--front { left: 35px; }
  .side-label--back { right: 28px; }
</style>
</head>
<body>

<section class="card card--front" aria-label="Card front">
  <div class="band band--front-left"></div>
  <div class="band band--front-bottom"></div>
  <div class="panel">
    <div class="front-brand">
      <div class="front-brand__name">MARLOW</div>
      <div class="front-brand__tagline">HEALTHY KITCHEN &nbsp;|&nbsp; MEAL PREP</div>
    </div>
  </div>
</section>

<section class="card card--back" aria-label="Card back">
  <div class="band band--back-top"></div>
  <div class="band band--back-right"></div>
  <div class="panel">
    <div class="back-brand">
      <div class="back-brand__name">MARLOW</div>
      <div class="back-brand__tagline">HEALTHY KITCHEN | MEAL PREP</div>
    </div>

    <h2 class="heading heading--attention">ATTENTION!!</h2>
    <p class="delivery"><strong>Delivery Promo!</strong><br>Order from us on the @hopmorsel app or @vantrelcourier</p>

    <div class="friday-box">
      <div class="friday-box__rule friday-box__rule--left"></div>
      <div class="friday-box__rule friday-box__rule--right"></div>
      <span class="friday-box__small friday-box__lead">app on</span>
      <span class="friday-box__days">FRIDAYS</span>
      <span class="friday-box__small friday-box__receive">and receive a</span>
      <span class="friday-box__free">FREE Sample</span>
      <span class="friday-box__small friday-box__detail">of our one of our meal prep meals in</span>
      <span class="friday-box__bag">your bag!</span>
    </div>

    <h2 class="heading heading--know">DID YOU KNOW?</h2>
    <p class="know-body">Meal Prep is another great service that we offer. Saving you time, promoting your health, and best of all providing a delicious lunch.</p>

    <div class="more-info">
      <span class="more-info__label">You can find more info on</span>
      <div class="more-info__rule more-info__rule--top"></div>
      <div class="more-info__rule more-info__rule--bottom"></div>
      <span class="more-info__site">www.<span>marlowpantry</span>.example</span>
    </div>
  </div>
  <div class="promo-strip">All orders are available for delivery or pickup!</div>
</section>

<div class="side-label side-label--front">Side-1</div>
<div class="side-label side-label--back">Side-2</div>

</body>
</html>
```